Clean Chic Simple Black & White One sided Biz Card

I need a business card for my company Brief Matter Arrangers. We are a luxury, white glove service for organizing files for attorneys.
I would like something that is stunningly simple and chic/sexy. This is going to be only one sided. We are going to use raised ink or ink embossing for the printing. So the logo will be raised in black. I am currently waiting to hear back from the printer as to whether or not the logo has to be in all black or can be left in its current state of black with grey initials. Please check our website for inspiration. www.briefmatterarrangers.example.
Thank you so much for your time.

* Please decide whichever title you think looks best(Chief Executive Officer, CEO, or President)
Updates

I really like the designs that make the logo large and the main focus.  
I also like the use of modern, masculine, simple, chic fonts for the slogan and info.

1) No bold font on slogan or info
2) Shrink info to be smaller maybe to make the logo bigger and more the focus
3) Maybe use grey for all the info and slogan so the focus will be on the logo

Thank you so much for your time!!

Target Market(s)

Luxury driven lawyers and their support staff

Industry/Entity Type

Printer

Requirements
Must have
• One sided card

Modern, sleek, masculine, chic, simple font.

Please add our slogan. Refer to file labeled "old logo" to see how we added our slogan under the old logo.
The slogan is, "We Bring Calm to Every Case File"

Please include the info below:
Marion Tullbeck (Chief Executive Officer, CEO, or President)
812 North Halvering Avenue, Suite 1400
Los Angeles, California 90071
P: (213)555-0182 F: (213)555-0167
mariont@briefmatterarrangers.example
www.briefmatterarrangers.example

Please refer to attached file labeled "inkpressingembossing requirements" for requirements from my printer. Thank you!
Nice to have
• It can be super simple with just the logo and my info. Or it could maybe have some cool feature. Just clean please.

I would prefer the info not be in bold. I think this will help the Logo stand out as the main focus.

I attached files of how the ink pressing and embossing will look.
Should not have
• No crazy shapes and no color other than black with a white background. The logo should be the focus since it will be embossed.

```html
<!DOCTYPE html>
<html lang="en">
<head>
<meta charset="utf-8">
<title>Brief Matter Arrangers — Business Card</title>
<link rel="stylesheet" href="https://fonts.googleapis.com/css2?family=Cabin:wght@400&family=Libre+Baskerville:ital@1&display=swap">
<style>
  :root {
    --backdrop: #3b3b3b;
    --card: #fbfbfa;
    --ink: #111111;
    --ink-grey: #555555;
    --mark-grey: #8a8a8a;
    --rule: #222222;
  }
  * { box-sizing: border-box; margin: 0; padding: 0; }
  html, body {
    width: 1200px;
    height: 715px;
    overflow: hidden;
    background: var(--backdrop);
  }
  .card {
    position: absolute;
    left: 75px;
    top: 57px;
    width: 1050px;
    height: 600px;
    background: var(--card);
    border-radius: 4px;
    font-family: "Cabin", sans-serif;
    font-weight: 400;
    font-style: normal;
    color: var(--ink);
  }
  .brand {
    position: absolute;
    left: 0;
    right: 0;
    top: 40px;
    display: flex;
    flex-direction: column;
    align-items: center;
    padding-left: 120px;
  }
  .brand-circle {
    width: 96px;
    height: 96px;
    border-radius: 50%;
    background: var(--mark-grey);
    margin-bottom: 18px;
  }
  .brand-name {
    font-size: 27px;
    font-weight: 400;
    letter-spacing: 0.22em;
    text-transform: uppercase;
    color: var(--ink);
  }
  .brand-slogan {
    margin-top: 8px;
    font-family: "Libre Baskerville", serif;
    font-style: italic;
    font-weight: 400;
    font-size: 19px;
    color: var(--ink-grey);
  }
  .person {
    position: absolute;
    left: 90px;
    top: 250px;
  }
  .person-name {
    font-size: 30px;
    font-weight: 400;
    text-transform: uppercase;
    letter-spacing: 0.02em;
    color: var(--ink-grey);
  }
  .person-title {
    margin-top: 6px;
    font-size: 20px;
    line-height: 1.25;
    color: var(--ink-grey);
  }
  .person-links {
    list-style: none;
    margin-top: 18px;
    font-size: 19px;
    line-height: 1.35;
    color: var(--ink-grey);
  }
  .divider {
    position: absolute;
    left: 480px;
    top: 360px;
    width: 1.5px;
    height: 130px;
    background: var(--rule);
  }
  .contact {
    position: absolute;
    left: 510px;
    top: 365px;
    font-size: 21px;
    font-style: normal;
    font-weight: 400;
    line-height: 1.3;
    color: var(--ink);
  }
  .contact .address { margin-top: 22px; }
</style>
</head>
<body>
  <main class="card">
    <header class="brand">
      <div class="brand-circle" aria-hidden="true"></div>
      <h1 class="brand-name">Brief Matter Arrangers, Inc.</h1>
      <p class="brand-slogan">“We Bring Calm to Every Case File”</p>
    </header>

    <section class="person">
      <h2 class="person-name">Marion Tullbeck</h2>
      <p class="person-title">Chief Executive Officer, CEO,<br>or President</p>
      <ul class="person-links">
        <li>mariont@briefmatterarrangers.example</li>
        <li>www.briefmatterarrangers.example</li>
      </ul>
    </section>

    <div class="divider" aria-hidden="true"></div>

    <address class="contact">
      <div>P: (213) 555-0182</div>
      <div>F: (213) 555-0167</div>
      <div class="address">812 North Halvering Avenue, Suite 1400<br>Los Angeles, California 90071</div>
    </address>
  </main>
</body>
</html>
```